Automotive supply company required new wiper blade packaging designs

I require packaging design for my new range of wiper blades, I will supply the die lines. Please consider my logo and its colors with your design. The industry is mechanical workshops. There will be some imagery provided by me, please contact me if you need more to complete your design. The range of wipers are " Frame Wiper Blades" and " Soft Wiper Blades" in various sizes. The soft wiper blades use various adapters, these adapters should be shown on the packaging. The frame wipers do not use adapters.There is a packaging example in my brief that you can use, although i am not the original artist so i cannot provide extra assistants with the pictures etc. Fennux images will provide many examples of wiper blade packaging. Once your design is complete there will be some additional information we can work on to complete the actual packaging, but nothing major. Good luck and i look forward to working with you.
Updates

Designs look the same

Target Market(s)

Mechanics

Industry/Entity Type

Automotive Part

Requirements
Must have
• My company logo colors, images of the adapters
• NAME OF WIPERS SHOULD BE
• " ZOLTEX FRAME WIPERS"
• " ZOLTEX SOFT WIPERS"

```html
<!DOCTYPE html>
<html lang="en">
<head>
<meta charset="utf-8">
<title>Vorkan Frame Wiper Blades – 14 inch pack</title>
<link rel="stylesheet" href="https://fonts.googleapis.com/css2?family=Barlow+Semi+Condensed:wght@400;600;700&family=Barlow:wght@400;700&display=swap">
<style>
  :root {
    --backdrop: #e4e4e4;
    --pack-black: #141414;
    --pack-black-soft: #232323;
    --pack-orange: #f47a12;
    --pack-blue: #0a87cf;
    --pack-blue-light: #2aa6e6;
    --text-white: #f2f2f2;
    --text-dark: #111111;
    --silver: #c9c9c9;
  }
  html, body {
    margin: 0;
    padding: 0;
    width: 788px;
    height: 1200px;
    overflow: hidden;
    background: var(--backdrop);
  }
  .canvas {
    position: relative;
    width: 788px;
    height: 1200px;
  }
  .pack-front {
    position: absolute;
    left: 335px;
    top: 50px;
    width: 118px;
    height: 1100px;
  }
  .size-label {
    font-family: "Barlow Semi Condensed", sans-serif;
    font-weight: 700;
    fill: var(--text-dark);
  }
  .size-metric {
    font-family: "Barlow", sans-serif;
    font-size: 7px;
    fill: var(--text-white);
  }
  .brand-name {
    font-family: "Barlow", sans-serif;
    font-weight: 700;
    font-size: 15px;
    letter-spacing: 1px;
    fill: var(--pack-blue-light);
  }
  .range-title {
    font-family: "Barlow Semi Condensed", sans-serif;
    font-weight: 700;
    font-size: 58px;
    fill: var(--text-white);
  }
  .range-subtitle {
    font-family: "Barlow Semi Condensed", sans-serif;
    font-weight: 400;
    font-size: 58px;
    fill: var(--pack-orange);
  }
</style>
</head>
<body>
<div class="canvas">
  <svg class="pack-front" viewBox="0 0 118 1100" xmlns="http://www.w3.org/2000/svg">
    <defs>
      <linearGradient id="blue-fade" x1="0" y1="0" x2="0" y2="1">
        <stop offset="0" stop-color="#0a87cf"/>
        <stop offset="1" stop-color="#0a7fc4"/>
      </linearGradient>
      <linearGradient id="blade-tone" x1="0" y1="0" x2="1" y2="0">
        <stop offset="0" stop-color="#1b1b1b"/>
        <stop offset="1" stop-color="#3a3a3a"/>
      </linearGradient>
    </defs>

    <!-- body bands -->
    <rect class="band-black" x="0" y="0" width="118" height="1100" fill="var(--pack-black)"/>
    <polygon class="band-orange" points="0,0 118,0 118,26 0,92" fill="var(--pack-orange)"/>
    <polygon class="band-blue" points="0,773 118,713 118,1100 0,1100" fill="url(#blue-fade)"/>

    <!-- size -->
    <text class="size-label" x="52" y="52" font-size="40" text-anchor="middle">14"</text>
    <text class="size-metric" x="30" y="85" transform="rotate(-29 30 85)">14inch / 356mm</text>

    <!-- brand -->
    <circle cx="59" cy="118" r="13" fill="none" stroke="var(--silver)" stroke-width="2"/>
    <text class="brand-name" x="59" y="155" text-anchor="middle">VORKAN</text>

    <!-- range title, reading top to bottom -->
    <g transform="translate(40 182) rotate(90)">
      <text x="0" y="0"><tspan class="range-title">FRAME WIPER </tspan><tspan class="range-subtitle">Blades</tspan></text>
    </g>

    <!-- product illustration -->
    <rect class="blade-visual" x="40" y="752" width="44" height="340" rx="3" fill="url(#blade-tone)" opacity="0.85" role="img" aria-label="Frame wiper blade product illustration"/>

    <!-- feature icon badge -->
    <circle cx="58" cy="733" r="18" fill="var(--silver)" stroke="#ffffff" stroke-width="1.5"/>
    <path d="M46 728 Q58 718 70 728 L66 740 L50 740 Z" fill="none" stroke="var(--text-dark)" stroke-width="1.6"/>
    <line x1="58" y1="740" x2="64" y2="726" stroke="var(--text-dark)" stroke-width="1.6"/>
  </svg>
</div>
</body>
</html>
```